We need a car wrap design. We sell air conditioning and solar panels.
The car model is a Dovalle Tarvimo L2 2019.

Industry/Entity Type

Air Conditioning and solar panels

Requirements
Must have
• My logo

```html
<!DOCTYPE html>
<html lang="pt">
<head>
<meta charset="utf-8">
<title>NORVA – Van Wrap Concepts</title>
<link rel="stylesheet" href="https://fonts.googleapis.com/css2?family=Poppins:wght@500;600;700&display=swap">
<style>
  :root {
    --brand-blue: #234a93;
    --brand-orange: #e0671d;
    --accent-yellow: #c9d21f;
    --panel-white: #ffffff;
    --canvas: #f3f3f1;
    --panel-edge: #d9d9d6;
  }
  html, body {
    margin: 0;
    width: 1200px;
    height: 1200px;
    overflow: hidden;
    background: var(--canvas);
    font-family: "Poppins", sans-serif;
  }
  .sheet {
    position: relative;
    width: 1200px;
    height: 1200px;
  }
  .wrap-panel {
    position: absolute;
    left: 90px;
    width: 1020px;
    height: 360px;
    background: var(--panel-white);
    border: 1px solid var(--panel-edge);
    border-radius: 28px 60px 18px 18px;
    overflow: hidden;
  }
  .wrap-panel--straight { top: 140px; }
  .wrap-panel--diagonal { top: 700px; }
  .wrap-graphics {
    position: absolute;
    inset: 0;
    width: 100%;
    height: 100%;
  }
  .brand {
    position: absolute;
    display: flex;
    align-items: center;
    gap: 18px;
  }
  .brand-dot {
    width: 58px;
    height: 58px;
    border-radius: 50%;
    background: var(--brand-blue);
  }
  .brand-name {
    font-weight: 600;
    font-size: 100px;
    line-height: 1;
    color: var(--brand-blue);
    letter-spacing: 2px;
  }
  .tagline {
    position: absolute;
    margin: 0;
    font-weight: 500;
    font-size: 11px;
    line-height: 1;
    letter-spacing: 2.2px;
    color: var(--brand-orange);
    text-transform: uppercase;
    white-space: nowrap;
  }
  .web {
    position: absolute;
    font-weight: 600;
    font-size: 24px;
    line-height: 1;
    letter-spacing: 4px;
    color: var(--panel-white);
    white-space: nowrap;
  }
  .phone {
    position: absolute;
    font-weight: 700;
    font-size: 30px;
    line-height: 1;
    letter-spacing: 3px;
    white-space: nowrap;
  }
  .wrap-panel--straight .brand { left: 60px; top: 20px; }
  .wrap-panel--straight .tagline { left: 195px; top: 130px; }
  .wrap-panel--straight .web { left: 130px; top: 161px; }
  .wrap-panel--straight .phone { left: 505px; top: 158px; color: var(--panel-white); }

  .wrap-panel--diagonal .brand { left: 60px; top: 26px; }
  .wrap-panel--diagonal .tagline { left: 195px; top: 134px; transform: rotate(3deg); transform-origin: left; }
  .wrap-panel--diagonal .web { left: 125px; top: 166px; transform: rotate(6.5deg); transform-origin: left; }
  .wrap-panel--diagonal .phone { left: 560px; top: 134px; color: var(--brand-blue); }
</style>
</head>
<body>
<main class="sheet">

  <section class="wrap-panel wrap-panel--straight" aria-label="Wrap concept with horizontal bands">
    <svg class="wrap-graphics" viewBox="0 0 1020 360" aria-hidden="true">
      <path d="M0 150 H870 Q960 150 1020 95 V140 Q965 195 890 195 H0 Z" fill="var(--brand-orange)"/>
      <path d="M0 205 H895 Q975 205 1020 155 V360 H0 Z" fill="var(--brand-blue)"/>
    </svg>
    <div class="brand">
      <span class="brand-dot"></span>
      <span class="brand-name">NORVA</span>
    </div>
    <p class="tagline">Soluções de Climatização e Energia</p>
    <span class="web">www.norva.com</span>
    <span class="phone">1480 27396</span>
  </section>

  <section class="wrap-panel wrap-panel--diagonal" aria-label="Wrap concept with diagonal bands">
    <svg class="wrap-graphics" viewBox="0 0 1020 360" aria-hidden="true">
      <polygon points="0,140 1020,255 1020,290 0,190" fill="var(--brand-orange)"/>
      <polygon points="0,200 1020,300 1020,360 0,360" fill="var(--brand-blue)"/>
      <polygon points="0,232 1020,318 1020,324 0,238" fill="var(--accent-yellow)"/>
    </svg>
    <div class="brand">
      <span class="brand-dot"></span>
      <span class="brand-name">NORVA</span>
    </div>
    <p class="tagline">Soluções de Climatização e Energia</p>
    <span class="web">www.norva.com</span>
    <span class="phone">1480 27396</span>
  </section>

</main>
</body>
</html>
```